Business Card for a Mortgage Agent (myself)

I need a business card for my new job as Mortgage Agent. The Broker's logo is to be on the card as well as the brokerage License number. Not sure if to include a photo or not. Info to be on card.
Dante Roux
Mortgage Agent
Lic # M47105386
Cell: 905-614-2753
Email: danterouxk.ma@fennmail.com
Web: www.karlvostermortgages.com
TPW Brokerage Lic. # 73918

```html
<!DOCTYPE html>
<html lang="en">
<head>
<meta charset="utf-8">
<title>Dante Roux – Mortgage Agent Business Card</title>
<link rel="stylesheet" href="https://fonts.googleapis.com/css2?family=Montserrat:wght@400;500;700&display=swap">
<style>
  :root {
    --stage: #3a3a3a;
    --stage-edge: #1e1e1e;
    --navy: #221a6b;
    --navy-deep: #1b1458;
    --gold: #ffc907;
    --white: #ffffff;
    --ink: #231c5e;
  }
  * { box-sizing: border-box; margin: 0; padding: 0; }
  html, body { width: 1200px; height: 900px; overflow: hidden; }
  body {
    background: radial-gradient(ellipse at 50% 40%, var(--stage) 0%, var(--stage-edge) 100%);
    font-family: "Montserrat", sans-serif;
    position: relative;
  }
  .card {
    position: absolute;
    left: 320px;
    width: 560px;
    height: 320px;
    background: var(--navy);
    overflow: hidden;
    box-shadow: 0 14px 30px rgba(0,0,0,0.45);
  }
  .card--front { top: 100px; }
  .card--back { top: 480px; }

  .front__band { position: absolute; inset: 0; }

  .agent { position: absolute; left: 28px; top: 52px; }
  .agent__name {
    color: var(--gold);
    font-weight: 700;
    font-size: 30px;
    letter-spacing: 1px;
    text-transform: uppercase;
    line-height: 1;
  }
  .agent__title {
    color: var(--white);
    font-size: 13px;
    letter-spacing: 1.5px;
    text-transform: uppercase;
    margin-top: 6px;
  }

  .contact {
    position: absolute;
    left: 28px;
    top: 148px;
    list-style: none;
    color: var(--ink);
    font-size: 13px;
    font-weight: 500;
    line-height: 1.75;
  }
  .contact__item { display: flex; align-items: center; gap: 7px; }
  .contact__icon { width: 11px; height: 11px; flex: none; }

  .brand {
    position: absolute;
    color: var(--white);
    font-weight: 500;
    text-transform: uppercase;
  }
  .brand__mark { display: flex; align-items: center; gap: 12px; }
  .brand__square { background: var(--gold); flex: none; }
  .brand__name { letter-spacing: 2px; }
  .brand__license { letter-spacing: 1px; }

  .card--front .brand { right: 32px; top: 96px; text-align: right; }
  .card--front .brand__mark { justify-content: flex-end; font-size: 62px; line-height: 1; letter-spacing: 2px; }
  .card--front .brand__square { width: 26px; height: 26px; }
  .card--front .brand__name { font-size: 13px; margin-top: 10px; }
  .card--front .brand__license { font-size: 8px; margin-top: 5px; }

  .card--back .brand { left: 0; right: 0; top: 88px; text-align: center; }
  .card--back .brand__mark { justify-content: center; font-size: 74px; line-height: 1; letter-spacing: 6px; }
  .card--back .brand__square { width: 32px; height: 32px; }
  .card--back .brand__name { font-size: 15px; margin-top: 14px; letter-spacing: 3px; }
  .card--back .brand__license { font-size: 9px; margin-top: 8px; }
</style>
</head>
<body>

<section class="card card--front" aria-label="Business card front">
  <svg class="front__band" width="560" height="320" viewBox="0 0 560 320" aria-hidden="true">
    <polygon points="0,126 262,126 420,320 0,320" fill="var(--gold)"/>
    <polygon points="28,126 38,116 38,126" fill="var(--white)"/>
  </svg>

  <div class="agent">
    <h1 class="agent__name">Dante Roux</h1>
    <p class="agent__title">Mortgage Agent</p>
  </div>

  <ul class="contact">
    <li class="contact__item">Lic # M47105386</li>
    <li class="contact__item">
      <svg class="contact__icon" viewBox="0 0 12 12" aria-hidden="true"><path d="M2.5 1 L4.5 1 L5.3 3.5 L4 4.6 C4.7 6 5.9 7.3 7.4 8 L8.5 6.7 L11 7.5 L11 9.5 C11 10.3 10.3 11 9.5 11 C5.4 11 1 6.6 1 2.5 C1 1.7 1.7 1 2.5 1 Z" fill="var(--ink)"/></svg>
      905-614-2753
    </li>
    <li class="contact__item">
      <svg class="contact__icon" viewBox="0 0 12 12" aria-hidden="true"><rect x="1" y="2.5" width="10" height="7" fill="none" stroke="var(--ink)" stroke-width="1.3"/><path d="M1 2.8 L6 6.6 L11 2.8" fill="none" stroke="var(--ink)" stroke-width="1.3"/></svg>
      danterouxk.ma@fennmail.com
    </li>
    <li class="contact__item">
      <svg class="contact__icon" viewBox="0 0 12 12" aria-hidden="true"><circle cx="6" cy="6" r="5" fill="none" stroke="var(--ink)" stroke-width="1.2"/><ellipse cx="6" cy="6" rx="2.2" ry="5" fill="none" stroke="var(--ink)" stroke-width="1"/><line x1="1" y1="6" x2="11" y2="6" stroke="var(--ink)" stroke-width="1"/></svg>
      www.karlvostermortgages.com
    </li>
  </ul>

  <div class="brand">
    <div class="brand__mark"><span class="brand__square"></span><span>TPW</span></div>
    <p class="brand__name">Trillium Peak Wealth</p>
    <p class="brand__license">License #73918</p>
  </div>
</section>

<section class="card card--back" aria-label="Business card back">
  <div class="brand">
    <div class="brand__mark"><span class="brand__square"></span><span>TPW</span></div>
    <p class="brand__name">Trillium Peak Wealth</p>
    <p class="brand__license">License #73918</p>
  </div>
</section>

</body>
</html>
```